Business Card for Industrial Distributor

We need a business card design for an industrial distributor. We sell machine parts for the manufacturing and oil industry. We would like the cards to look clean and modern but with a touch of industry.

Our colors are blue/white.

Please feel free to visit our website www.korvanlineusa.com

Target Market(s)

mexican manufacturers in the automobile/aerospace industry

Industry/Entity Type

Industrial

Colors
ffffff
0555a3

```html
<!DOCTYPE html>
<html lang="en">
<head>
<meta charset="utf-8">
<title>Korvanline Business Card</title>
<link rel="stylesheet" href="https://fonts.googleapis.com/css2?family=Roboto:wght@300;400;700;900&family=Roboto+Condensed:wght@300;400;700&display=swap">
<style>
  :root {
    --brand-blue: #0555a3;
    --band-blue: #13498f;
    --white: #ffffff;
    --stripe-grey: #9a9a9a;
    --ink: #1c1c1c;
    --muted: #7a7a7a;
    --band-text: #b9c8df;
    --backdrop: #2b2d31;
  }
  * { margin: 0; padding: 0; box-sizing: border-box; }
  html, body { width: 1200px; height: 900px; overflow: hidden; }
  body {
    background: var(--backdrop);
    display: flex;
    align-items: center;
    justify-content: center;
    gap: 48px;
    font-family: "Roboto", sans-serif;
  }
  .card {
    width: 540px;
    height: 310px;
    border-radius: 22px;
    overflow: hidden;
    position: relative;
  }

  /* Front */
  .card-front { background: var(--white); }
  .front-brand {
    position: absolute;
    left: 40px; top: 44px;
    display: flex; align-items: center; gap: 10px;
  }
  .brand-dot {
    width: 40px; height: 40px; border-radius: 50%;
    background: var(--brand-blue);
  }
  .brand-name {
    font-family: "Roboto", sans-serif;
    font-weight: 900;
    font-size: 44px;
    letter-spacing: -0.5px;
    color: var(--brand-blue);
  }
  .holder {
    position: absolute;
    right: 40px; top: 112px;
    display: flex; align-items: stretch; gap: 10px;
    text-align: right;
  }
  .holder-name {
    font-family: "Roboto Condensed", sans-serif;
    font-size: 26px;
    font-weight: 700;
    color: var(--ink);
    line-height: 1.05;
  }
  .holder-name .first { color: var(--brand-blue); }
  .holder-name .last { font-weight: 400; }
  .holder-role {
    font-family: "Roboto Condensed", sans-serif;
    font-weight: 300;
    font-size: 14px;
    letter-spacing: 0.5px;
    color: var(--muted);
    margin-top: 4px;
  }
  .holder-bar { width: 4px; background: var(--brand-blue); }
  .stripe {
    position: absolute; left: 0; right: 0;
    top: 196px; height: 10px;
    background: var(--stripe-grey);
  }
  .contact-band {
    position: absolute; left: 0; right: 0;
    top: 206px; bottom: 0;
    background: var(--band-blue);
    display: flex; justify-content: space-between; align-items: center;
    padding: 0 36px;
    font-family: "Roboto Condensed", sans-serif;
    font-size: 14px;
    line-height: 1.5;
    color: var(--band-text);
  }
  .contact-address { text-align: right; font-size: 15px; }

  /* Back */
  .card-back {
    background: var(--brand-blue);
    display: flex; flex-direction: column;
    align-items: center; justify-content: center;
  }
  .back-brand { display: flex; align-items: center; gap: 14px; }
  .card-back .brand-dot { width: 54px; height: 54px; background: var(--white); }
  .card-back .brand-name { font-size: 60px; color: var(--white); }
  .back-web {
    align-self: flex-end;
    margin-right: 70px; margin-top: 6px;
    display: flex; align-items: center; gap: 6px;
    font-size: 15px; font-weight: 300;
    letter-spacing: 0.5px;
    color: var(--white);
  }
</style>
</head>
<body>
  <section class="card card-front">
    <div class="front-brand">
      <span class="brand-dot"></span>
      <span class="brand-name">Korvanline</span>
    </div>
    <div class="holder">
      <div>
        <div class="holder-name"><span class="first">MARCUS</span> <span class="last">HALE</span></div>
        <div class="holder-role">MARKETING HEAD</div>
      </div>
      <span class="holder-bar"></span>
    </div>
    <div class="stripe"></div>
    <div class="contact-band">
      <div class="contact-lines">
        <div>Tel: (555) 214 - 3307</div>
        <div>Email: sales@korvanlineusa.com</div>
        <div>Web: korvanlineusa.com</div>
      </div>
      <div class="contact-address">
        <div>Fax: (555) 214 - 3311</div>
        <div>4120 Harbor Mill Rd.</div>
        <div>Riverton, TX 78410</div>
      </div>
    </div>
  </section>

  <section class="card card-back">
    <div class="back-brand">
      <span class="brand-dot"></span>
      <span class="brand-name">Korvanline</span>
    </div>
    <div class="back-web">
      <svg width="13" height="13" viewBox="0 0 14 14" fill="none" stroke="#ffffff" stroke-width="1.1" aria-hidden="true">
        <circle cx="7" cy="7" r="6"/>
        <ellipse cx="7" cy="7" rx="2.6" ry="6"/>
        <line x1="1" y1="7" x2="13" y2="7"/>
      </svg>
      <span>korvanlineusa.com</span>
    </div>
  </section>
</body>
</html>
```